Ember&Willow

I'm writing a book and need a front and back cover for the book.

IMPORTANT DETAILS:
TITLE: Ember & Willow
SUBTITLE: Twelve empowering true stories of women who found strength and hope in times of darkness and despair.
AUTHORS: Marta Pellworth & Dalia Vurnek
1. The book is about WOMEN'S stories of struggle (EMBER) and overcoming them with a hopeful and inspiring story at the end (WILLOW). So the cover of the book should depict these opposing / conflicting ideas.

2. The cover needs to be clean and simple

3. a.The font for the word EMBER should look stronger/bolder/more intense/sturdier/a little more masculine....
b. The ampersand (&) between Ember & Willow should tie the two fonts together
c. The font for the word WILLOW should look fluid/clean/EASY-TO-READ cursive script

4. I'm open to different color fonts with a limit of 3 colors MAX

5. For the back cover: This will be a collection of stories from 12 total authors so the back cover needs to have room for 12 faces somehow.

Looking forward to it.

```html
<!DOCTYPE html>
<html lang="en">
<head>
<meta charset="UTF-8">
<title>Ember &amp; Willow — Book Cover</title>
<link rel="stylesheet" href="https://fonts.googleapis.com/css2?family=Cormorant+Garamond:wght@500;600&family=Parisienne&family=Cinzel:wght@400;500&display=swap">
<style>
  :root {
    --backdrop: #a2a2a2;
    --paper: #ffffff;
    --teal: #4a7379;
    --band: #547b82;
    --ink: #2e2222;
    --crimson: #a3183a;
    --coral: #e5553b;
    --umber: #5a1f17;
    --cocoa: #2c1410;
  }
  * { margin: 0; padding: 0; box-sizing: border-box; }
  html, body {
    width: 1200px;
    height: 1151px;
    overflow: hidden;
    background: var(--backdrop);
  }
  .cover {
    position: absolute;
    left: 283px;
    top: 100px;
    width: 634px;
    height: 951px;
    background: var(--paper);
    overflow: hidden;
  }
  .title {
    position: absolute;
    left: 0;
    top: 0;
    width: 100%;
    height: 350px;
    color: var(--teal);
    font-weight: normal;
  }
  .title-strong {
    position: absolute;
    left: 38px;
    top: 96px;
    font-family: "Cormorant Garamond", serif;
    font-weight: 600;
    font-size: 96px;
    letter-spacing: 1px;
    line-height: 1;
    white-space: nowrap;
  }
  .title-amp {
    position: absolute;
    left: 366px;
    top: 8px;
    font-family: "Parisienne", cursive;
    font-size: 186px;
    line-height: 1;
  }
  .title-script {
    position: absolute;
    left: 200px;
    top: 168px;
    font-family: "Parisienne", cursive;
    font-size: 146px;
    line-height: 1.2;
    white-space: nowrap;
  }
  .subtitle {
    position: absolute;
    left: 0;
    top: 362px;
    width: 100%;
    text-align: center;
    font-family: "Cinzel", serif;
    font-weight: 400;
    font-size: 15px;
    line-height: 28.5px;
    letter-spacing: 0.5px;
    text-transform: uppercase;
    color: var(--ink);
  }
  .artwork {
    position: absolute;
    left: 0;
    top: 470px;
    width: 634px;
    height: 412px;
    display: block;
  }
  .author-band {
    position: absolute;
    left: 0;
    top: 881px;
    width: 100%;
    height: 34px;
    background: var(--band);
    color: var(--paper);
    font-family: "Cinzel", serif;
    font-size: 18px;
    letter-spacing: 2.6px;
    line-height: 34px;
    text-transform: uppercase;
    text-align: center;
    white-space: nowrap;
  }
</style>
</head>
<body>
  <main class="cover">
    <h1 class="title" aria-label="Ember &amp; Willow">
      <span class="title-strong">EMBER</span>
      <span class="title-amp">&amp;</span>
      <span class="title-script">willow</span>
    </h1>

    <p class="subtitle">
      Twelve empowering true stories of women<br>
      who found strength and hope in<br>
      times of darkness and despair.
    </p>

    <svg class="artwork" viewBox="0 0 634 412" role="img" aria-label="Illustration of five women of diverse backgrounds standing together in profile">
      <defs>
        <linearGradient id="artwork-tone" x1="0" y1="0" x2="1" y2="1">
          <stop offset="0" stop-color="var(--crimson)"/>
          <stop offset="0.45" stop-color="var(--coral)"/>
          <stop offset="0.75" stop-color="var(--umber)"/>
          <stop offset="1" stop-color="var(--cocoa)"/>
        </linearGradient>
      </defs>
      <rect x="0" y="0" width="634" height="412" fill="url(#artwork-tone)" opacity="0.85"/>
    </svg>

    <div class="author-band">Marta Pellworth &amp; Dalia Vurnek</div>
  </main>
</body>
</html>
```